We need a mobile and desktop design for our new online store, Fair Dinkum Finds. The website's goals is to help Australian manufacturers and inventors sell their goods online.

The site needs to match the them of our logo.
Updates

Project Deadline Extended
Reason: We are extending the deadline because we have been away for Easter and was unable to answer everyone's questions.

Thank you for everyone's questions. I'm sorry for the delay in my answer. I have been away. We do not need the site coded. My coders have asked for a graphic they can cut up.

While we don't need anyone to code the site. If the choosen designer does a great job and is easy to work with, it highly likely we will hire them for future work. We have been running a business online for ten years and are short a graphic designer at the moment. It is fair to think of this as the first stage of a job interview.

The target market is Australian consumers. The website is a marketing portal for Australian producers/manufacturers/inventors to sell their goods online.

We will be helping companies who are brilliant at making goods but need some help selling them online.

Each company will have it''s own store on the site. The companies lined up so far include a chocolate manufacturer, kitchen sponge manufacturer, curry producer and surfboard maker. The range of stores will vary. We are looking for an overall design to work from.

We are basins the function of the store design on NerdCrate.com store and our existing store you can view at www.thriftwisehub.com.au/store. I also like Blue Kite days and Wavemart.com.au

I'm sorry, we are not going to guarantee payment. Just in case, none of the designs are appropriate. But, this is the third time we have used Sketch Swarm and we paid for both previous jobs. We are not here to waste time.

If you have any more questions. Fire away. I''m sorry, my last brief was a bit too brief. It was my last task before rushing to a school presentation.

I'm looking forward to seeing everyone's designs and hopefully meeting a new designer.

Here is a link to our first mock up of the site created by our coders. Ignore the graphics and text. (It was the boys putting something there to work from.) The URL is:-

www.fairdinkumfinds.com

The stores motto is...

"We only sell goods that are Fair Dinkum Finds!"

Our goals are..

To help Australian manufacturers, inventors and producers. People who are good at making items and are adding value to Australia, but are so busy making their goods that they struggle selling them online.

Of the designs we have seen so far, I prefer the blue and white based designs, instead of the red adn white. Because, the red ones seem to make the site look more bloody then brilliant :-)

All businesses/stores will be given a Gold, Bronze or Silver ranking, depending on how much of their work benefits Australia.

Thank you for everyone's designs so far. The quality of the designs have been excellent! Our team will be discussing them on Thursday. I'll post an update on Friday morning

All the best,

Maree

Target Market(s)

Australians, general

Industry/Entity Type

Store

Requirements
Must have
• Online store

```html
<!DOCTYPE html>
<html lang="en">
<head>
<meta charset="utf-8">
<title>Fair Dinkum Finds – Store</title>
<link href="https://fonts.googleapis.com/css2?family=PT+Sans:ital,wght@0,400;0,700;1,400;1,700&family=Roboto+Condensed:wght@400;700&display=swap" rel="stylesheet">
<style>
:root{
  --blue:#1a9ae0;
  --heading:#1473b8;
  --nav:#4f4f51;
  --text:#333;
  --white:#fff;
  --page:#fff;
  --footer-top:#5fcdf4;
  --footer-bottom:#1594d6;
  --bar:#4fb0df;
  --grey-line:#d6d6d6;
  --tone-silver:#b9b9b9;
  --tone-gold:#c9973a;
  --tone-straw:#bcae90;
  --tone-plum:#6a4c4c;
  --tone-leaf:#7d7a36;
  --tone-bronze:#8a5a34;
  --tone-slate:#4a4e58;
  --tone-cream:#ece8d2;
}
*{box-sizing:border-box;margin:0;padding:0}
html,body{width:1018px;height:1200px;overflow:hidden;background:var(--page)}
body{position:relative;font-family:"PT Sans",sans-serif;color:var(--text)}
.abs{position:absolute}

/* header */
.header{left:153px;top:0;width:713px;height:83px;background:var(--blue)}
.brand{left:18px;top:24px;display:flex;align-items:center;gap:8px;color:var(--white);font-weight:700;font-size:17px;line-height:1}
.brand-dot{width:14px;height:14px;border-radius:50%;background:var(--white)}
.util-links{right:12px;top:9px;display:flex;gap:10px;font-size:7px;color:var(--white);text-transform:uppercase;letter-spacing:.2px}
.search{left:425px;top:54px;width:121px;height:14px;background:var(--white);border-radius:2px;font-size:6px;color:#888;padding:3px 6px}
.search svg{position:absolute;right:4px;top:2px}
.checkout{left:561px;top:32px;width:142px;height:40px;background:var(--white);border-radius:2px}
.checkout svg{position:absolute;left:12px;top:7px}
.checkout .t1{position:absolute;left:48px;top:10px;font-size:8.5px;color:#444}
.checkout .t2{position:absolute;left:48px;top:22px;font-size:9px;color:var(--blue)}

.nav{left:153px;top:83px;width:713px;height:25px;background:var(--nav);color:var(--white);font-size:7.5px;text-transform:uppercase}
.nav span{position:absolute;top:8px;letter-spacing:-.1px}

/* hero */
.hero{left:153px;top:112px;width:713px;height:170px;background:linear-gradient(90deg,#cfe7f3 0%,#7cb9dd 30%,#1a82c2 60%,#0e6aa6 100%);overflow:hidden}
.hero-fade{left:122px;top:112px;width:31px;height:170px;background:linear-gradient(90deg,#fff,#e9f2f8)}
.hero-photo{left:0;top:0;width:430px;height:170px;background:linear-gradient(90deg,#d8ebf5 0%,#b9d5e6 35%,#6fa7cc 75%,rgba(26,130,194,0) 100%)}
.hero-line{right:34px;color:var(--white);font-style:italic;font-weight:700;font-size:25px;letter-spacing:-1px;text-align:right;white-space:nowrap}
.dots{right:10px;top:154px;display:flex;gap:2px}
.dots i{width:7px;height:7px;background:#5ea7d6;display:block}
.dots i:first-child{background:var(--white)}

/* products */
.section-band{left:153px;top:284px;width:713px;height:42px;background:linear-gradient(#fff,#e6e6e6)}
.section-band h2{position:absolute;left:14px;top:13px;font-family:"Roboto Condensed",sans-serif;font-weight:700;font-size:14px;color:var(--heading)}
.product{width:164px;height:181px}
.product .photo{width:164px;height:137px}
.product .label{position:absolute;left:0;top:137px;width:164px;height:44px;background:var(--blue);color:var(--white)}
.product .name{position:absolute;left:11px;top:8px;font-size:7px;text-transform:uppercase;letter-spacing:-.1px}
.product .price{position:absolute;left:11px;top:21px;font-family:"Roboto Condensed",sans-serif;font-size:14px}

.pager{top:733px;height:20px;font-size:8px}
.pager a{position:absolute;top:0;height:20px;border:1px solid #c4c4c4;border-radius:2px;background:linear-gradient(#fafafa,#e2e2e2);color:#444;text-align:center;line-height:18px;text-decoration:none}
.pager a.blue{background:linear-gradient(#3e9ae0,#1466b2);color:var(--white);border-color:#14589a}

.divider{left:153px;top:771px;width:713px;height:2px;background:var(--grey-line)}
.col h3{font-family:"Roboto Condensed",sans-serif;font-weight:700;font-size:14px;color:var(--heading);margin-bottom:7px}
.col p{font-size:7.4px;line-height:13px;color:#222}
.vsep{top:793px;width:1px;height:110px;background:var(--grey-line)}
.btn{height:21px;background:var(--blue);color:var(--white);font-size:7.5px;text-transform:uppercase;display:flex;align-items:center;justify-content:center;gap:3px}
.field-label{font-size:7px;color:var(--heading);font-weight:700}
.field{height:17px;border:1px solid #c9c9c9;background:var(--white)}

/* footer */
.footer{left:0;top:932px;width:1018px;height:228px;background:linear-gradient(var(--footer-top),var(--footer-bottom))}
.fcol{top:33px}
.fcol h4{font-weight:400;font-size:14.5px;color:#21507a;margin-bottom:6px}
.fcol ul{list-style:none}
.fcol li{font-size:10px;color:var(--white);line-height:18.2px}
.fsep{top:34px;width:1px;height:140px;background:rgba(255,255,255,.35)}
.social li{display:flex;align-items:center;gap:7px;line-height:20.4px}
.social li i{width:17px;height:17px;border-radius:50%;background:#111;display:block}
.bottom-bar{left:0;top:1160px;width:1018px;height:40px;background:var(--bar);font-size:9.5px;color:#21507a}
</style>
</head>
<body>

<header class="abs header">
  <div class="abs brand"><i class="brand-dot"></i>Fair Dinkum Finds</div>
  <div class="abs util-links"><span>Your Account</span><span>|</span><span>Blog</span><span>|</span><span>Help</span><span>|</span><span>Contact</span></div>
  <div class="abs search">SEARCH : :
    <svg width="10" height="10" viewBox="0 0 10 10"><circle cx="4" cy="4" r="3" fill="none" stroke="#555" stroke-width="1.2"/><line x1="6" y1="6" x2="9" y2="9" stroke="#555" stroke-width="1.6"/></svg>
  </div>
  <div class="abs checkout">
    <svg width="30" height="26" viewBox="0 0 30 26"><path d="M3 8h24l-3 14H6z" fill="#1a8fd6"/><path d="M9 8l6-6 6 6" fill="none" stroke="#1a8fd6" stroke-width="2"/><path d="M8 12v7M12 12v7M16 12v7M20 12v7M24 12v7" stroke="#fff" stroke-width="1.2"/></svg>
    <span class="t1">CHECKOUT</span>
    <span class="t2">3 ITEMS : $25 AUD</span>
  </div>
</header>

<nav class="abs nav">
  <span style="left:21px">About FDF</span>
  <span style="left:105px">Blog</span>
  <span style="left:172px">All Stores</span>
  <span style="left:260px">Your Account</span>
  <span style="left:364px">Shipping &amp; Accounts</span>
  <span style="left:490px">Contact FDF</span>
</nav>

<div class="abs hero-fade"></div>
<section class="abs hero">
  <div class="abs hero-photo" role="img" aria-label="Smiling shopper holding shopping bags and a phone in a bright mall"></div>
  <div class="abs hero-line" style="top:54px">We only sell</div>
  <div class="abs hero-line" style="top:84px">goods that are Fair Dinkum Finds!</div>
  <div class="abs dots"><i></i><i></i><i></i><i></i></div>
</section>

<div class="abs section-band"><h2>PRODUCTS</h2></div>

<div class="abs product" style="left:153px;top:339px"><div class="photo" role="img" aria-label="Wine preserver spray beside a wine bottle and glass" style="background:var(--tone-silver)"></div><div class="label"><span class="name">Wine and your waistline</span><span class="price">$34.99</span></div></div>
<div class="abs product" style="left:336px;top:339px"><div class="photo" role="img" aria-label="Block of cheese with slices on a plate" style="background:var(--tone-gold)"></div><div class="label"><span class="name">Wine and your waistline</span><span class="price">$34.99</span></div></div>
<div class="abs product" style="left:519px;top:339px"><div class="photo" role="img" aria-label="Woven straw hat with fabric roses" style="background:var(--tone-straw)"></div><div class="label"><span class="name">Wine and your waistline</span><span class="price">$34.99</span></div></div>
<div class="abs product" style="left:702px;top:339px"><div class="photo" role="img" aria-label="Stack of food and wine books" style="background:var(--tone-plum)"></div><div class="label"><span class="name">Wine and your waistline</span><span class="price">$34.99</span></div></div>

<div class="abs product" style="left:153px;top:535px"><div class="photo" role="img" aria-label="Red tulips in a garden" style="background:var(--tone-leaf)"></div><div class="label"><span class="name">Wine and your waistline</span><span class="price">$34.99</span></div></div>
<div class="abs product" style="left:336px;top:535px"><div class="photo" role="img" aria-label="Antique pocket watch on a wooden table" style="background:var(--tone-bronze)"></div><div class="label"><span class="name">Wine and your waistline</span><span class="price">$34.99</span></div></div>
<div class="abs product" style="left:519px;top:535px"><div class="photo" role="img" aria-label="Wine bottles resting in an iron rack" style="background:var(--tone-slate)"></div><div class="label"><span class="name">Wine and your waistline</span><span class="price">$34.99</span></div></div>
<div class="abs product" style="left:702px;top:535px"><div class="photo" role="img" aria-label="Produce freshness packets on a white background" style="background:var(--tone-cream)"></div><div class="label"><span class="name">Wine and your waistline</span><span class="price">$34.99</span></div></div>

<div class="abs pager" style="left:0;width:1018px">
  <a class="blue" style="left:617px;width:44px">« Prev</a>
  <a style="left:664px;width:19px">1</a>
  <a style="left:686px;width:19px">2</a>
  <a style="left:709px;width:19px">3</a>
  <a class="blue" style="left:731px;width:19px">...</a>
  <a style="left:754px;width:19px">4</a>
  <a style="left:777px;width:19px">5</a>
  <a style="left:799px;width:19px">6</a>
  <a class="blue" style="left:822px;width:44px">Next »</a>
</div>

<div class="abs divider"></div>

<div class="abs col" style="left:153px;top:790px;width:210px">
  <h3>ABOUT FDF</h3>
  <p>Lorem ipsum dolor sit amet, consectetur adipiscing elit.<br>Donec congue arcu eget ipsum iaculis ornare. Nulla semper,<br>tortor sed dapibus laoreet, ante tortor feugiat risus, id placerat<br>nunc mi quis enim. Fusce sollicitudin diam a tellus molestie<br>pellentesque. Nam et massa et enim.</p>
</div>
<div class="abs btn" style="left:153px;top:888px;width:73px">Read more <svg width="9" height="7" viewBox="0 0 9 7"><path d="M1 1l2.5 2.5L1 6M5 1l2.5 2.5L5 6" fill="none" stroke="#fff" stroke-width="1.4"/></svg></div>
<div class="abs vsep" style="left:379px"></div>

<div class="abs col" style="left:404px;top:790px;width:215px">
  <h3>DONEC VENENATIS</h3>
  <p>Lorem ipsum dolor sit amet, consectetur adipiscing elit.<br>Donec congue arcu eget ipsum iaculis ornare. Nulla semper,<br>tortor sed dapibus laoreet, ante tortor feugiat risus, id placerat<br>nunc mi quis enim. Fusce sollicitudin diam a tellus molestie<br>pellentesque. Nam et massa et enim.</p>
</div>
<div class="abs btn" style="left:404px;top:888px;width:73px">Read more <svg width="9" height="7" viewBox="0 0 9 7"><path d="M1 1l2.5 2.5L1 6M5 1l2.5 2.5L5 6" fill="none" stroke="#fff" stroke-width="1.4"/></svg></div>
<div class="abs vsep" style="left:634px"></div>

<div class="abs col" style="left:660px;top:790px;width:210px">
  <h3>NEWSLETTER SIGNUP</h3>
  <p>Lorem ipsum dolor sit amet, consectetur adipiscing elit.<br>Donec congue arcu eget.</p>
</div>
<span class="abs field-label" style="left:662px;top:845px">Name :</span>
<span class="abs field-label" style="left:769px;top:845px">Email :</span>
<div class="abs field" style="left:661px;top:858px;width:97px"></div>
<div class="abs field" style="left:768px;top:858px;width:98px"></div>
<div class="abs btn" style="left:660px;top:888px;width:73px">Signup <svg width="9" height="7" viewBox="0 0 9 7"><path d="M1 1l2.5 2.5L1 6M5 1l2.5 2.5L5 6" fill="none" stroke="#fff" stroke-width="1.4"/></svg></div>

<footer class="abs footer">
  <div class="abs fcol" style="left:155px"><h4>Information</h4><ul><li>Home</li><li>About Our Products</li><li>Buy or Selling</li><li>Delivery</li><li>Latest Product</li></ul></div>
  <div class="abs fsep" style="left:259px"></div>
  <div class="abs fcol" style="left:288px"><h4>Producs</h4><ul><li>Home</li><li>About Our Products</li><li>Buy or Selling</li><li>Delivery</li><li>Latest Product</li></ul></div>
  <div class="abs fsep" style="left:392px"></div>
  <div class="abs fcol" style="left:418px"><h4>About Company</h4><ul><li>About Us</li><li>Why Choose Us</li><li>Testimonials</li><li>News</li><li>Blog Posts</li></ul></div>
  <div class="abs fsep" style="left:536px"></div>
  <div class="abs fcol" style="left:566px"><h4>Support</h4><ul><li>Support</li><li>FAQ</li><li>Resources</li><li>Delivery &amp; orders</li><li>Contact Info</li></ul></div>
  <div class="abs fsep" style="left:666px"></div>
  <div class="abs fcol social" style="left:701px"><h4>Get Connected</h4><ul><li><i></i>FaceSpace</li><li><i></i>Chirper</li><li><i></i>LinkUp</li><li><i></i>RSS</li></ul></div>
</footer>

<div class="abs bottom-bar">
  <span class="abs" style="left:156px;top:15px">Copyright © 2013 Company name.&nbsp; All Rights Reserved.</span>
  <span class="abs" style="right:160px;top:15px">Privacy Policy&nbsp; | &nbsp;Terms of Services</span>
</div>

</body>
</html>
```